Brochure design for Velicor

Create a bi-fold A5 size brochure. I have attached our logo and the written content to be included in the brochure. So the brochure will have a total of 4 pages (front page, inner two pages, back page). End source files need to include final printable brochure as well as editable files.

```html
<!DOCTYPE html>
<html lang="en">
<head>
<meta charset="utf-8">
<title>Velicor brochure – front cover</title>
<link rel="stylesheet" href="https://fonts.googleapis.com/css2?family=Quicksand:wght@600&family=Lexend:wght@300&display=swap">
<style>
  :root {
    --backdrop: #ffffff;
    --brand-blue: #1f6fb6;
    --brand-green: #86c23d;
    --photo-light: #e3e7ea;
    --photo-mid: #b4c3c7;
    --photo-teal: #8fd0cb;
    --photo-dark: #5f6f76;
    --photo-rose: #c9a9b3;
    --white: #ffffff;
  }
  * { box-sizing: border-box; margin: 0; padding: 0; }
  html, body {
    width: 1200px; height: 1200px; overflow: hidden;
    background: var(--backdrop);
  }
  .cover {
    position: absolute; left: 196px; top: 30px;
    width: 789px; height: 1120px; overflow: hidden;
    background: var(--photo-mid);
  }
  .cover-photo {
    position: absolute; inset: 0;
    background:
      radial-gradient(ellipse 42% 10% at 52% 19%, rgba(200,236,232,.85), transparent 70%),
      radial-gradient(ellipse 38% 14% at 45% 30%, rgba(240,248,248,.75), transparent 70%),
      radial-gradient(ellipse 45% 22% at 72% 55%, rgba(143,208,203,.75), transparent 70%),
      radial-gradient(ellipse 30% 16% at 86% 44%, rgba(230,240,240,.7), transparent 70%),
      radial-gradient(ellipse 30% 25% at 8% 62%, rgba(201,169,179,.8), transparent 70%),
      radial-gradient(ellipse 35% 12% at 25% 42%, rgba(235,240,242,.8), transparent 70%),
      radial-gradient(ellipse 28% 18% at 40% 68%, rgba(95,111,118,.55), transparent 70%),
      radial-gradient(ellipse 30% 8% at 50% 98%, rgba(201,169,179,.6), transparent 70%),
      linear-gradient(180deg, var(--photo-light) 0%, #d6dde0 22%, #7f9298 23%, #a8babf 30%, var(--photo-mid) 50%, #94a7ad 70%, #c4cdd2 100%);
  }
  .brand {
    position: absolute; left: 0; right: 0; top: 100px;
    text-align: center; color: var(--brand-blue);
    font-family: "Quicksand", sans-serif; font-weight: 600;
  }
  .brand-name {
    display: inline-flex; align-items: center; gap: 14px;
    font-size: 58px; line-height: 1;
  }
  .brand-dot {
    width: 22px; height: 22px; border-radius: 50%;
    background: var(--brand-blue);
  }
  .brand-tagline {
    margin-top: 8px; font-size: 16px; letter-spacing: .2px;
  }
  .message-band {
    position: absolute; left: 0; right: 0; top: 785px; height: 268px;
    background: linear-gradient(90deg, rgba(31,111,182,.97) 0%, rgba(31,111,182,.72) 28%, rgba(134,194,61,.6) 62%, rgba(134,194,61,.97) 100%);
    color: var(--white); text-align: center;
    font-family: "Lexend", sans-serif; font-weight: 300;
  }
  .headline {
    margin-top: 44px; font-size: 32px; line-height: 45px;
    font-weight: 300; letter-spacing: .3px;
  }
  .subline {
    margin-top: 19px; font-size: 25px; line-height: 36px;
    font-weight: 300;
  }
</style>
</head>
<body>
  <main class="cover">
    <div class="cover-photo" role="img" aria-label="Close-up laboratory photo of a glass petri dish with a pipette releasing a droplet, in soft teal and grey tones"></div>
    <header class="brand">
      <div class="brand-name"><span class="brand-dot"></span>Velicor</div>
      <p class="brand-tagline">Personalised Health &amp; Wellness</p>
    </header>
    <section class="message-band">
      <h1 class="headline">A revolution in health &amp; wellness has<br>been brewing – and now it is here!</h1>
      <p class="subline">Precision health and wellness is tailored<br>to your unique genetic make-up.</p>
    </section>
  </main>
</body>
</html>
```